We are a church and would like a flyer for a special service that is held once a quarter to get families and friends to come out to join us. See below content and details for sizes.
Church Name: Covenant Harvest Global Fellowship
Church Logo : Attached
Title : Family and Friends Day
Subtitle: Strengthening Families - Connecting Relationships
Host: Bishop Kwame Dantor (file attached. Don't need full body. Please crop)
Date: Sunday, 24 May
Time: 9:30 AM
Address: 2917 Marlow Lane, Suite F, Bowie MD, 20716
Phone : 240 593 2186
Website: www.chgfellowship.org
Flyer Size: Facebook size 851 x 314 pixels, Flash size 680 x 340 & Power Point size Standard

```html
<!DOCTYPE html>
<html lang="en">
<head>
<meta charset="utf-8">
<title>Family &amp; Friends Day — Covenant Harvest Global Fellowship</title>
<link rel="stylesheet" href="https://fonts.googleapis.com/css2?family=Lobster&family=Marcellus&family=Open+Sans:wght@400;700&family=Roboto+Condensed:wght@300;400&display=swap">
<style>
  :root {
    --ink: #1b1b1f;
    --navy: #1f2a44;
    --rule: #222226;
    --label-bg: #ffffff;
    --value-tint: rgba(244, 214, 205, 0.85);
    --value-edge: rgba(214, 150, 160, 0.55);
    --host-muted: #e6d9e6;
    --host-name: #ffffff;
    --frame: #6d6566;
  }
  * { box-sizing: border-box; margin: 0; padding: 0; }
  html, body { width: 1200px; height: 600px; overflow: hidden; }
  body { background: #ffffff; }

  .flyer {
    position: relative;
    width: 1200px;
    height: 600px;
    overflow: hidden;
    background:
      radial-gradient(ellipse 380px 230px at 720px 280px, rgba(255,250,232,0.95), rgba(255,246,226,0) 100%),
      radial-gradient(ellipse 520px 260px at 600px 230px, rgba(252,240,224,0.9), rgba(252,240,224,0) 100%),
      radial-gradient(ellipse 420px 220px at 560px 620px, rgba(250,176,120,0.85), rgba(250,176,120,0) 100%),
      radial-gradient(ellipse 420px 260px at 60px 600px, rgba(214,62,110,0.95), rgba(214,62,110,0) 100%),
      radial-gradient(ellipse 420px 300px at 1180px 600px, rgba(120,52,120,0.95), rgba(120,52,120,0) 100%),
      radial-gradient(ellipse 360px 260px at 1180px 40px, rgba(40,140,200,0.9), rgba(40,140,200,0) 100%),
      radial-gradient(ellipse 420px 260px at 40px 40px, rgba(170,220,232,0.95), rgba(170,220,232,0) 100%),
      linear-gradient(180deg, #bfe0e8 0%, #f1e5dc 45%, #d9849a 100%);
  }

  .church-mark {
    position: absolute;
    left: 22px; top: 4px;
    width: 104px; height: 104px;
    border-radius: 50%;
    background: radial-gradient(circle, rgba(255,255,255,0.9) 0%, rgba(255,255,255,0.35) 60%, rgba(255,255,255,0) 100%);
  }
  .church-name {
    position: absolute;
    left: 145px; top: 48px;
    font-family: "Roboto Condensed", sans-serif;
    font-weight: 400;
    font-size: 14.5px;
    letter-spacing: 1.4px;
    text-transform: uppercase;
    color: var(--navy);
  }

  .event-title {
    position: absolute;
    left: 0; width: 1200px; top: 112px;
    text-align: center;
    font-family: "Lobster", cursive;
    font-size: 82px;
    font-weight: 400;
    letter-spacing: 2px;
    color: var(--ink);
  }
  .rule {
    position: absolute;
    left: 145px; width: 912px; height: 2px;
    background: var(--rule);
  }
  .rule--top { top: 211px; }
  .rule--bottom { top: 259px; }
  .event-tagline {
    position: absolute;
    left: 0; width: 1200px; top: 220px;
    text-align: center;
    font-family: "Marcellus", serif;
    font-size: 27px;
    color: #2e2e33;
  }
  .event-tagline .star { font-size: 22px; margin: 0 8px; vertical-align: 2px; }

  .detail {
    position: absolute;
    display: flex;
    height: 42px;
    background: var(--label-bg);
    padding: 3px 15px 3px 0;
  }
  .detail__label {
    width: 133px;
    padding-left: 17px;
    font-family: "Open Sans", sans-serif;
    font-weight: 700;
    font-size: 20px;
    line-height: 36px;
    color: var(--ink);
  }
  .detail__value {
    flex: 1;
    padding-left: 14px;
    font-family: "Open Sans", sans-serif;
    font-weight: 400;
    font-size: 21px;
    line-height: 36px;
    color: var(--ink);
    background: linear-gradient(90deg, var(--value-edge), var(--value-tint) 30%, rgba(250,236,228,0.9));
  }
  .detail--date    { left: 43px;  top: 317px; width: 445px; }
  .detail--time    { left: 500px; top: 317px; width: 445px; }
  .detail--phone   { left: 43px;  top: 384px; width: 445px; }
  .detail--website { left: 500px; top: 384px; width: 445px; }
  .detail--address { left: 43px;  top: 450px; width: 902px; }

  .host-portrait {
    position: absolute;
    left: 974px; top: 336px;
    width: 176px; height: 176px;
    border-radius: 50%;
    border: 8px solid var(--frame);
    background: radial-gradient(circle at 50% 45%, #8a7c76 0%, #5b504d 55%, #3c3434 100%);
  }

  .host {
    position: absolute;
    left: 838px; top: 534px;
    font-family: "Roboto Condensed", sans-serif;
    white-space: nowrap;
  }
  .host__role { font-weight: 300; font-size: 18px; color: var(--host-muted); margin-right: 14px; }
  .host__name { font-weight: 400; font-size: 26px; color: var(--host-name); letter-spacing: 0.3px; }
</style>
</head>
<body>
  <main class="flyer">
    <div class="church-mark" aria-hidden="true"></div>
    <p class="church-name">Covenant Harvest Global Fellowship</p>

    <h1 class="event-title">Family &amp; Friends Day</h1>
    <div class="rule rule--top"></div>
    <p class="event-tagline">Strengthening Families<span class="star">★</span>Connecting Relationships</p>
    <div class="rule rule--bottom"></div>

    <div class="detail detail--date"><span class="detail__label">Date</span><span class="detail__value">24 May 2015 (Sunday)</span></div>
    <div class="detail detail--time"><span class="detail__label">Time</span><span class="detail__value">9:30 AM</span></div>
    <div class="detail detail--phone"><span class="detail__label">Phone</span><span class="detail__value">240 593 2186</span></div>
    <div class="detail detail--website"><span class="detail__label">Website</span><span class="detail__value">www.chgfellowship.org</span></div>
    <div class="detail detail--address"><span class="detail__label">Address</span><span class="detail__value">2917 Marlow Lane, Suite F, Bowie MD, 20716.</span></div>

    <div class="host-portrait" role="img" aria-label="Cropped portrait photo of the host, Bishop Kwame Dantor"></div>
    <p class="host"><span class="host__role">Host</span><span class="host__name">Bishop Kwame Dantor</span></p>
  </main>
</body>
</html>
```